Tech Company Letterhead/Business Cards/Envelopes

We would like a new stationary design for a technology company that develops full turnkey solutions for governments related to Data, Identity Tracking, Fingerprinting, Passport Control, and Border Protection Systems.

We would like the stationary designs to include:

Letter Head
Business Cards
Envelopes

Target Market(s)

Corporate

Industry/Entity Type

Business

Contact Information for Business Card

Details to be shared with the winner.

Font styles to use
Serif
Sans Serif

Colors
e4daeb
85abd2
3176b5
0355a3
0692cd

```html
<!DOCTYPE html>
<html lang="en">
<head>
<meta charset="utf-8">
<title>Novix Stationery</title>
<link href="https://fonts.googleapis.com/css2?family=Carlito:wght@400;700&family=Open+Sans:wght@400;600;700&display=swap" rel="stylesheet">
<style>
:root{
  --bg:#dedede;
  --paper:#fafafa;
  --blue:#0a6cbf;
  --blue-deep:#0769b3;
  --grey:#4b4b4b;
  --text:#2b2b2b;
  --muted:#6d6d6d;
}
*{margin:0;padding:0;box-sizing:border-box}
html,body{width:1200px;height:947px;overflow:hidden}
body{background:var(--bg);position:relative;font-family:"Carlito",sans-serif;color:var(--text)}
.wordmark{font-family:"Carlito",sans-serif;font-weight:700;color:var(--blue);letter-spacing:.06em;line-height:1;position:absolute}
.sheet{position:absolute;background:var(--paper);box-shadow:0 1px 4px rgba(0,0,0,.25)}
.footer-bar{position:absolute;left:0;right:0;bottom:0;display:flex}
.footer-bar .bar-blue{background:var(--blue);height:100%}
.footer-bar .bar-grey{background:var(--grey);height:100%}
.contact{position:absolute;font-family:"Open Sans",sans-serif;color:var(--muted)}
.contact p{display:flex;align-items:center;gap:4px;white-space:nowrap}
.ico{display:inline-block;border:1px solid var(--muted);border-radius:50%;flex:none}

/* letterhead */
.letterhead{left:36px;top:45px;width:607px;height:859px}
.letterhead .wordmark{left:36px;top:36px;font-size:40px}
.letterhead .contact{right:35px;top:33px;font-size:9px;line-height:14px;text-align:right}
.letterhead .contact p{justify-content:flex-end}
.letterhead .ico{width:9px;height:9px}
.letter-body{position:absolute;left:43px;top:165px;width:522px;font-size:10.2px;line-height:19px;text-align:justify}
.signoff{position:absolute;left:43px;top:636px;font-size:10.2px;line-height:19px}
.signature{display:block;width:64px;height:38px;margin:2px 0 4px 12px;background:linear-gradient(135deg,#e6e6e6,#cfcfcf);border-radius:3px}
.letterhead .footer-bar{height:9px}

/* standalone mark */
.brand-mark{left:884px;top:72px;font-size:58px}

/* business card */
.card-front{left:672px;top:450px;width:240px;height:144px}
.card-front .wordmark{left:24px;top:54px;font-size:20px}
.card-name{position:absolute;left:38px;top:80px;font-family:"Open Sans",sans-serif;font-size:6.5px;color:var(--blue)}
.card-divider{position:absolute;left:132px;top:46px;width:1px;height:52px;background:var(--grey)}
.card-front .contact{left:138px;top:45px;font-size:5px;line-height:9.6px}
.card-front .ico{width:5px;height:5px}
.card-front .footer-bar{height:4px}
.card-back{left:930px;top:449px;width:240px;height:143px;background:var(--blue-deep)}
.card-back .wordmark{color:#fff;left:0;right:0;text-align:center;top:56px;font-size:30px}

/* envelope */
.envelope{left:672px;top:630px;width:494px;height:197px;overflow:hidden}
.envelope .wordmark{left:15px;top:26px;font-size:27px}
.flap{position:absolute;right:0;top:0;width:84px;height:197px}
.env-name{position:absolute;left:16px;top:141px;font-family:"Open Sans",sans-serif;font-weight:700;font-size:8.5px;letter-spacing:.12em;color:var(--blue)}
.envelope .contact{left:16px;top:153px;font-size:6px;line-height:9.5px}
.envelope .ico{width:6px;height:6px}
.envelope .footer-bar{height:4px;right:84px}
</style>
</head>
<body>

<section class="sheet letterhead">
  <div class="wordmark">NOVIX</div>
  <div class="contact">
    <p><span class="ico"></span>Example&nbsp; Example&nbsp; Example&nbsp; Example&nbsp; Example</p>
    <p><span class="ico"></span>00 0000 0000 <span class="ico"></span>00 0000 0000 <span class="ico"></span>00 0000 0000</p>
    <p><span class="ico"></span>info@novix.com.us <span class="ico"></span>www.novix.com.us</p>
  </div>
  <div class="letter-body">
    <p>Dear Sir/Mam,</p>
    <p>Lorem Ipsum is simply dummy text of the printing and typesetting industry. Lorem Ipsum has been the industry's standard dummy text ever since the 1500s, when an unknown printer took a galley of type and scrambled it to make a type specimen book. It has survived not only five centuries, but also the leap into electronic typesetting, remaining essentially unchanged. It was popularised in the 1960s with the release of Letraset sheets containing Lorem Ipsum passages, and more recently with desktop publishing software like Aldus PageMaker including versions of Lorem Ipsum.</p>
    <p>Lorem Ipsum is simply dummy text of the printing and typesetting industry. Lorem Ipsum has been the industry's standard dummy text ever since the 1500s, when an unknown printer took a galley of type and scrambled it to make a type specimen book. It has survived not only five centuries, but also the leap into electronic typesetting, remaining essentially unchanged. It was popularised in the 1960s with the release of Letraset sheets containing Lorem Ipsum passages, and more recently with desktop publishing software like Aldus PageMaker including versions of Lorem Ipsum.</p>
    <p>Lorem Ipsum is simply dummy text of the printing and typesetting industry. Lorem Ipsum has been the industry's standard dummy text ever since the 1500s, when an unknown printer took a galley of type and scrambled it to make a type specimen book. It has survived not only five centuries, but also the leap into electronic typesetting, remaining essentially unchanged. It was popularised in the 1960s with the release of Letraset sheets containing Lorem Ipsum passages, and more recently with desktop publishing software like Aldus PageMaker including versions of Lorem Ipsum.</p>
  </div>
  <div class="signoff">
    <p>Your's faithfully</p>
    <span class="signature" role="img" aria-label="Handwritten signature"></span>
    <p>Novix Solutions</p>
  </div>
  <div class="footer-bar"><span class="bar-blue" style="width:470px;clip-path:polygon(0 0,100% 0,98.5% 100%,0 100%)"></span><span style="width:12px"></span><span class="bar-grey" style="flex:1;clip-path:polygon(3% 0,100% 0,100% 100%,0 100%)"></span></div>
</section>

<div class="wordmark brand-mark">NOVIX</div>

<section class="sheet card-front">
  <div class="wordmark">NOVIX</div>
  <div class="card-name">NAME EXAMPLE</div>
  <div class="card-divider"></div>
  <div class="contact">
    <p><span class="ico"></span>Example Example Example Example</p>
    <p><span class="ico"></span>00 0000 0000</p>
    <p><span class="ico"></span>00 0000 0000</p>
    <p><span class="ico"></span>00 0000 0000</p>
    <p><span class="ico"></span>info@novix.com.us</p>
    <p><span class="ico"></span>www.novix.com.us</p>
  </div>
  <div class="footer-bar"><span class="bar-blue" style="width:166px;clip-path:polygon(0 0,100% 0,97% 100%,0 100%)"></span><span style="width:4px"></span><span class="bar-grey" style="flex:1;clip-path:polygon(6% 0,100% 0,100% 100%,0 100%)"></span></div>
</section>

<section class="sheet card-back">
  <div class="wordmark">NOVIX</div>
</section>

<section class="sheet envelope">
  <div class="wordmark">NOVIX</div>
  <div class="env-name">Novix Solutions</div>
  <div class="contact">
    <p><span class="ico"></span>Example&nbsp; Example&nbsp; Example&nbsp; Example&nbsp; Example</p>
    <p><span class="ico"></span>00 0000 0000 <span class="ico"></span>00 0000 0000 <span class="ico"></span>00 0000 0000</p>
    <p><span class="ico"></span>info@novix.com.us <span class="ico"></span>www.novix.com.us</p>
  </div>
  <svg class="flap" viewBox="0 0 84 197" aria-hidden="true">
    <rect width="84" height="197" fill="var(--blue-deep)"/>
    <polygon points="0,0 84,0 84,10" fill="var(--paper)"/>
    <polygon points="0,197 84,197 84,187" fill="var(--paper)"/>
  </svg>
  <div class="footer-bar"><span class="bar-blue" style="width:320px;clip-path:polygon(0 0,100% 0,98.5% 100%,0 100%)"></span><span style="width:5px"></span><span class="bar-grey" style="flex:1;clip-path:polygon(4% 0,100% 0,100% 100%,0 100%)"></span></div>
</section>

</body>
</html>
```